dkfarrowplace website

I need a new homepage design for my current website at www.DKFarrowPlace.example. I want someone to look at my current website and develop a more appealing homepage... right now the colors don't blend very well and it needs a facelift

Reason: This has been extended to September 10th

```html
<!DOCTYPE html>
<html lang="en">
<head>
<meta charset="utf-8">
<title>D K Farrow — Homepage</title>
<link href="https://fonts.googleapis.com/css2?family=Open+Sans:wght@400;600;700&family=Great+Vibes&display=swap" rel="stylesheet">
<style>
:root{
  --pink:#f0626e;
  --pink-soft:#f47c86;
  --ink:#3a3a3a;
  --text:#555;
  --bar:#454545;
  --brown:#4b2f29;
  --brown-light:#7a5a50;
  --cream:#f4f1ee;
  --line:#d9d6d2;
  --blue:#3b87c4;
  --link:#3a6db0;
  --footer:#3d3d3d;
  --band:#e8e8e8;
}
*{margin:0;padding:0;box-sizing:border-box}
html,body{width:840px;height:1200px;overflow:hidden;background:#fff}
body{font-family:"Open Sans",Arial,sans-serif;color:var(--text);position:relative}
.topbar{height:20px;background:var(--bar);color:#eee;font-size:6.5px;letter-spacing:.4px;text-align:right;padding:6px 16px 0 0}
.nav{height:39px;display:flex;background:#fff;border-bottom:1px solid var(--line)}
.brand{width:131px;background:var(--pink);color:#fff;font-size:17px;font-weight:600;display:flex;align-items:center;padding-left:18px}
.menu{display:flex}
.menu a{display:flex;align-items:center;padding:0 14px;font-size:8.5px;font-weight:600;color:#444;text-decoration:none;border-right:1px solid var(--line)}
.menu a.active{color:var(--pink)}
.callus{width:128px;text-align:center;padding-top:7px;font-size:9px;color:#555;border-right:1px solid var(--line)}
.callus b{display:block;color:var(--pink);font-size:13px;font-weight:600;letter-spacing:.5px}
.social{flex:1;background:#e6e6e6;display:flex;align-items:center;justify-content:center;gap:5px}
.social span{font-size:7px;font-weight:600;color:#555}
.hero{position:relative;height:291px;background:linear-gradient(90deg,#3a221d 0%,var(--brown) 50%,#5a3a33 100%);overflow:hidden}
.hero-photo{position:absolute;left:0;top:0;width:270px;height:291px;background:radial-gradient(ellipse at 45% 45%,#a06e58 0%,#6a4438 55%,#3a221d 100%)}
.hero-wedge{position:absolute;left:0;top:0}
.hero-copy{position:absolute;left:292px;top:40px;color:#fff}
.hero-copy .script{font-family:"Great Vibes",cursive;font-size:40px;line-height:1}
.hero-copy .l1{font-size:26px;color:var(--pink-soft);margin-top:6px;letter-spacing:.5px}
.hero-copy .l2{font-size:26px;letter-spacing:.5px}
.hero-copy .l2 b{font-weight:700}
.hero-copy .l3{font-size:20px;margin-top:2px;letter-spacing:.5px}
.btn{display:inline-block;background:var(--pink);color:#fff;font-size:9px;font-weight:600;padding:5px 18px}
.hero-copy .btn{margin-top:16px}
.dots{position:absolute;left:555px;top:268px;display:flex;gap:4px}
.dots i{width:8px;height:8px;background:#fff}
.dots i.on{background:var(--pink)}
.side{position:absolute;left:622px;top:0;width:218px;height:291px;background:radial-gradient(ellipse at 55% 35%,#9a6c58 0%,#6d4a3f 60%,#4a322c 100%)}
.side-tag{position:absolute;left:0;top:172px;width:218px;height:73px;background:rgba(220,210,205,.55)}
.side-tag .big{position:absolute;left:16px;top:2px;font-size:40px;font-weight:700;color:#fff;line-height:1}
.side-tag .small{position:absolute;left:18px;top:44px;font-size:16px;font-weight:700;color:#fff}
.side-tag .stripe{position:absolute;right:0;top:0;width:26px;height:73px;background:var(--pink-soft)}
.side-tip{position:absolute;left:0;top:245px;width:218px;height:32px;background:rgba(50,35,30,.85);color:#fff}
.side-tip .n{position:absolute;left:4px;top:2px;width:18px;height:28px;background:var(--brown-light);font-size:20px;text-align:center;line-height:28px}
.side-tip .t{position:absolute;left:28px;top:5px;font-size:7px;line-height:1.3}
.side-tip em{font-style:italic}
.intro{position:absolute;top:350px;left:0;width:840px;height:244px;background:var(--cream)}
.video{position:absolute;left:28px;top:29px;width:165px;height:158px;background:#fff;border:1px solid var(--line);text-align:center}
.video .frame{margin:15px auto 0;width:133px;height:90px;background:linear-gradient(135deg,#5a3a55,#8a5b6e 50%,#3a5a7a);border:2px solid #bbb}
.video .cap{font-size:9px;font-weight:600;color:#333;margin-top:10px}
.video .view{font-size:8px;color:var(--pink)}
.about{position:absolute;left:207px;top:38px;width:268px}
.about h2,.report h2,.media h2{color:var(--pink);font-weight:400;font-size:17px}
.about p{font-size:7.6px;line-height:1.7;margin-top:6px}
.about .btn{margin-top:8px;padding:5px 22px}
.divider{position:absolute;left:490px;top:22px;width:1px;height:175px;background:#999}
.report{position:absolute;left:505px;top:20px;width:285px}
.report .cover{position:absolute;left:5px;top:0;width:34px;height:50px;background:linear-gradient(#e8eef4,#9fb3c8);border:1px solid #889}
.report h2{position:absolute;left:56px;top:12px;font-weight:600}
.report .sub{position:absolute;left:54px;top:33px;font-size:13px;color:#555;white-space:nowrap}
.report .lead{position:absolute;left:0;top:64px;font-size:7.6px;line-height:1.6;width:285px}
.field{position:absolute;top:112px;width:125px;height:22px;background:#fff;border:1px solid #ccc;border-radius:4px;font-size:8px;padding:6px 8px;color:#555}
.subscribe{position:absolute;left:0;top:140px;width:98px;height:20px;background:var(--blue);color:#fff;font-size:8.5px;font-weight:600;text-align:center;line-height:20px}
.report .privacy{position:absolute;left:0;top:167px;font-size:7.6px;line-height:1.6;width:285px}
.carousel{position:absolute;left:16px;top:562px;width:808px;height:146px}
.books{position:absolute;left:0;top:0}
.book{position:absolute;top:0;width:230px}
.book .cover{position:absolute;top:12px;width:70px;height:118px}
.book h3{position:absolute;left:84px;top:26px;font-size:8.8px;font-weight:600;color:#333;line-height:1.2;width:135px}
.book p{position:absolute;left:84px;top:55px;font-size:7.4px;line-height:1.55;width:140px}
.book a{color:var(--pink)}
.arrow{position:absolute;top:55px}
.media{position:absolute;left:49px;top:742px;width:545px}
.media p{font-size:7.6px;line-height:1.7;margin-top:4px}
.media .listen{display:block;margin-top:7px;font-size:9px;color:var(--link);text-decoration:underline}
.media-photo{position:absolute;left:607px;top:727px;width:179px;height:137px;background:linear-gradient(160deg,#b35a4a 0%,#8a6a55 45%,#3a3a3a 100%)}
.press{position:absolute;left:71px;top:884px;width:698px;height:41px;border:1px solid var(--line);display:flex;padding:4px 3px;gap:3px}
.press i{flex:1;background:#e4e1de}
.band{position:absolute;top:940px;left:0;width:840px;height:52px;background:var(--band);text-align:center;color:#666}
.band .main{font-size:13.5px;margin-top:10px}
.band .main b{font-weight:600;color:#555}
.band .note{font-size:8.5px;font-style:italic;color:#888}
.footer{position:absolute;top:992px;left:0;width:840px;height:208px;background:var(--footer);color:#fff}
.fnav{position:absolute;left:108px;top:42px;font-size:8.5px;font-weight:600}
.fbrand{position:absolute;left:108px;top:74px;font-size:15px;font-weight:600}
.faddr{position:absolute;left:108px;top:96px;font-size:9px;line-height:1.5;font-weight:600}
.faddr a{color:var(--pink);text-decoration:none;font-weight:400}
.flegal{position:absolute;left:108px;top:140px;font-size:9px;line-height:1.5;color:#ddd}
.flegal u{color:#fff}
.fsocial{position:absolute;top:145px;width:64px;height:19px;background:#e8e8e8;color:#3a5a8a;font-size:7.5px;font-weight:600;text-align:center;line-height:19px}
.likebox{position:absolute;left:546px;top:14px;width:150px;height:180px;background:#2f2f2f}
.likebox .ico{position:absolute;left:18px;top:14px;width:16px;height:16px;background:#6a8ac8}
.likebox .count{position:absolute;left:16px;top:64px;font-size:27px;letter-spacing:1px}
.likebox .msg{position:absolute;left:16px;top:102px;font-size:13px;line-height:1.2;color:#5b86d6}
.likebox .sig{position:absolute;left:20px;top:148px;font-size:12px;font-weight:600}
</style>
</head>
<body>
<div class="topbar">THE FLAVOR OF HEALTH : SPICES TEMPT YOUR TONGUE AND SAVE YOUR HEART</div>
<div class="nav">
  <div class="brand">D K Farrow</div>
  <nav class="menu">
    <a class="active">HOME</a><a>PRODUCTS</a><a>ABOUT US</a><a>BLOG</a><a>FORUM</a><a>MEDIA ROOM</a><a>SUCCESS STORIES</a>
  </nav>
  <div class="callus">Call Us Today!<b>555-013-4470</b></div>
  <div class="social"><span>Linkly</span><span>Chirper</span></div>
</div>

<section class="hero">
  <div class="hero-photo" role="img" aria-label="Portrait of the nutritionist smiling with arms crossed"></div>
  <svg class="hero-wedge" width="622" height="291" viewBox="0 0 622 291">
    <polygon points="420,291 622,210 622,291" fill="#7a5a50" opacity=".7"/>
  </svg>
  <div class="hero-copy">
    <div class="script">Discover</div>
    <div class="l1">SECRETS TO A</div>
    <div class="l2">SLIMMER<b>SEXIER</b></div>
    <div class="l3">&amp; HEALTHIER YOU!</div>
    <span class="btn">READ MORE</span>
  </div>
  <div class="dots"><i class="on"></i><i></i><i></i><i></i></div>
  <div class="side" role="img" aria-label="Portrait of the nutritionist in a brown top">
    <div class="side-tag"><div class="stripe"></div><div class="big">natural</div><div class="small">SOLUTIONS</div></div>
    <div class="side-tip"><div class="n">7</div><div class="t"><em>winter workout</em><br>TIPS TO STAY COMFORTABLE WHILE OUTDOORS</div></div>
  </div>
</section>

<section class="intro">
  <div class="video">
    <div class="frame" role="img" aria-label="Video still from a talk show appearance"></div>
    <div class="cap">Hal Benton Talk Show</div>
    <div class="view">Click to view</div>
  </div>
  <div class="about">
    <h2>ABOUT D K FARROW</h2>
    <p>D K Farrow is a nutritionist and certified weight-loss expert, passionate relationship/life coach, and inspirational speaker. She has been featured on The Hal Benton Morning Show, The Marlo Winters Show, The Jada Fenn Show, and The Miles Barden Show. D K has made appearances on national, regional and cable television stations, as well as in the pages of Lumen, Radiance, Pulse and Home Circle.</p>
    <span class="btn">READ MORE</span>
  </div>
  <div class="divider"></div>
  <div class="report">
    <div class="cover" role="img" aria-label="Free report cover"></div>
    <h2>FREE Report</h2>
    <div class="sub">“5 Reasons You Can’t Lose Weight!”</div>
    <div class="lead">Just enter your name and email below to get instant access to this 30 page report absolutely FREE!</div>
    <div class="field" style="left:0">Name</div>
    <div class="field" style="left:132px;top:110px">Email</div>
    <div class="subscribe">SUBSCRIBE</div>
    <div class="privacy"><em>E-mail Privacy:</em> Sign up with complete confidence! We will never sell, rent, lease, or share your information with anyone.</div>
  </div>
</section>

<section class="carousel">
  <svg class="books" width="808" height="146" viewBox="0 0 808 146">
    <polygon points="14,0 794,0 808,14 808,132 794,146 14,146 0,132 0,14" fill="#fff" stroke="#ddd"/>
    <line x1="276" y1="0" x2="276" y2="146" stroke="#ddd"/>
    <line x1="511" y1="0" x2="511" y2="146" stroke="#ddd"/>
  </svg>
  <svg class="arrow" style="left:20px" width="20" height="30" viewBox="0 0 20 30"><path d="M10 2 2 15 10 28M18 2 10 15 18 28" fill="none" stroke="#d8505c" stroke-width="1.6"/></svg>
  <svg class="arrow" style="left:768px" width="20" height="30" viewBox="0 0 20 30"><path d="M2 2 10 15 2 28M10 2 18 15 10 28" fill="none" stroke="#d8505c" stroke-width="1.6"/></svg>
  <div class="book" style="left:50px">
    <div class="cover" style="left:0;background:linear-gradient(#f4f6ec,#7fb24a)" role="img" aria-label="Green drink book cover"></div>
    <h3>The Fresh Start Blender Reset</h3>
    <p>The Fresh Start Blender Reset will jump-start your weight loss, increase your energy level, clear your mind, and improve your overall health...<br><a><u>Read More</u></a></p>
  </div>
  <div class="book" style="left:295px">
    <div class="cover" style="left:0;background:linear-gradient(#fbeef0,#e06a80)" role="img" aria-label="Trim waistline book cover"></div>
    <h3>Simple Steps to a Trimmer Middle!</h3>
    <p>All across America, people are struggling with stubborn belly fat. But you don’t have to be one of them! Are you ready to make a commitment to getting a slimmer, sexier waistline? <a><u>Read More</u></a></p>
  </div>
  <div class="book" style="left:536px">
    <div class="cover" style="left:0;background:linear-gradient(#f7c6d8,#d84c8c)" role="img" aria-label="Weight loss guide book cover"></div>
    <h3>Feel Lighter Without Strict Rules or Gyms!</h3>
    <p>Want to lose weight without counting calories, starving yourself, giving up your favorite foods, or eating bland packaged foods? Would you like to look and feel younger than you have in years? <a><u>Read More</u></a></p>
  </div>
</section>

<section class="media">
  <h2>Media Room</h2>
  <p>D K is a fabulous guest on radio and TV, and in magazines and newspapers. D K’s expertise is in high demand, with appearances on The Hal Benton Morning Show, The Marlo Winters Show, The Jada Fenn Show, and The Miles Barden Show. D K has made appearances on national, regional and cable television stations, as well as in the pages of Lumen, Radiance, Pulse and Home Circle. Since reclaiming her health, losing weight, and discovering “second youth” in her forties, bestselling author D K Farrow has become the voice of inspiration to women who want to lose weight, be healthy, and get their sexy back!</p>
  <a class="listen">Click Here to Listen to D K Farrow Featured on The Hal Benton Morning Show! &gt;&gt;</a>
</section>
<div class="media-photo" role="img" aria-label="Studio photo of the nutritionist with a talk show host"></div>

<div class="press" aria-label="Featured media outlets"><i></i><i></i><i></i><i></i><i></i><i></i><i></i><i></i></div>

<div class="band">
  <div class="main">Media Phone: <b>555-013-4470</b> (only media inquiries will get a return call)</div>
  <div class="note">Personal medical and health-related questions and inquiries will NOT receive a response.</div>
</div>

<footer class="footer">
  <div class="fnav">HOME | PRODUCTS | ABOUT US | BLOG | FORUM | MEDIA ROOM | SUCCESS STORIES</div>
  <div class="fbrand">D K Farrow</div>
  <div class="faddr">4820 Linden Row Suite 12 Brookhaven, ST 00415<br>For customer service support, contact <a>info@dkfarrowplace.example</a></div>
  <div class="flegal"><u>Privacy Policy</u> | <u>Terms of Use</u> | <u>Disclaimer</u><br>Copyright © 2011 Verdana Lane Press</div>
  <div class="fsocial" style="left:322px">Linkly</div>
  <div class="fsocial" style="left:392px">Chirper</div>
  <div class="likebox">
    <div class="ico"></div>
    <div class="count">16,373</div>
    <div class="msg">YOU LIKE US! YOU<br>REALLY LIKE US!</div>
    <div class="sig">D K Farrow</div>
  </div>
</footer>
</body>
</html>
```